Etiketten-Design für Himbeer-Gin
Zielgruppe
GIN
Aufgabenstellung
Wir benötigen ein Etikett für unseren neuen Himbeere GIN, der Name des GINs lautet: KorvalaGIN und soll für folgende Flasche dargestellt werden: https://www.flakoria-beispiel.de/luma-flasche-500ml-schwarz-beschichtet-tqx41-karton-48stk.html
mit dem Etikett https://klebmarken-beispiel.de/anwendungen/fluoreszierende-etiketten/ Himbeerlastiges Design mit bestehendem Logo (WendelGIN) siehe Daten. Bei Fragen stehe ich gerne zur Verfügung!

```html
<!DOCTYPE html>
<html lang="de">
<head>
<meta charset="utf-8">
<title>KorvalaGIN – Etikett</title>
<link rel="stylesheet" href="https://fonts.googleapis.com/css2?family=Oswald:wght@700&family=Space+Mono:wght@400;700&display=swap">
<style>
  :root {
    --label-bg: #221f1f;
    --raspberry: #f4268a;
    --ink-light: #f4f1f1;
  }
  * { margin: 0; padding: 0; box-sizing: border-box; }
  html, body {
    width: 1200px;
    height: 800px;
    overflow: hidden;
    background: var(--label-bg);
  }
  .label {
    position: relative;
    width: 1200px;
    height: 800px;
    background: var(--label-bg);
    overflow: hidden;
  }
  .berry-illustration {
    position: absolute;
    left: 667px;
    top: 0;
    width: 533px;
    height: 613px;
    background: radial-gradient(ellipse at 60% 45%, rgba(244, 38, 138, 0.28) 0%, rgba(244, 38, 138, 0.12) 45%, rgba(34, 31, 31, 0) 75%);
  }
  .product-name {
    position: absolute;
    left: 0;
    width: 1192px;
    text-align: center;
    font-family: "Oswald", sans-serif;
    font-weight: 700;
    font-size: 190px;
    line-height: 1;
    color: var(--raspberry);
    letter-spacing: 2px;
  }
  .product-name--main { top: 200px; }
  .product-name--type { top: 380px; }
  .alcohol {
    position: absolute;
    left: 443px;
    top: 652px;
    font-family: "Space Mono", monospace;
    font-weight: 700;
    font-size: 30px;
    letter-spacing: 5px;
    color: var(--ink-light);
    white-space: nowrap;
  }
  .origin {
    position: absolute;
    left: 447px;
    top: 703px;
    font-family: "Space Mono", monospace;
    font-size: 10px;
    letter-spacing: 3.4px;
    color: var(--ink-light);
    white-space: nowrap;
  }
  .side-panel {
    position: absolute;
    left: 34px;
    top: 748px;
    width: 680px;
    transform: rotate(-90deg);
    transform-origin: top left;
    color: var(--ink-light);
    font-family: "Space Mono", monospace;
  }
  .brewery-name {
    font-weight: 700;
    font-size: 18px;
    letter-spacing: 4px;
    line-height: 20px;
    white-space: nowrap;
  }
  .brewery-about {
    margin-top: 14px;
    font-size: 10px;
    line-height: 17.4px;
    letter-spacing: 1px;
    white-space: nowrap;
  }
  .accent-band {
    position: absolute;
    left: 0;
    top: 768px;
    width: 1200px;
    height: 10px;
    background: var(--raspberry);
  }
</style>
</head>
<body>
  <main class="label">
    <div class="berry-illustration" role="img" aria-label="Pinke Strichzeichnung eines Himbeerzweigs mit Blättern und zwei Himbeeren"></div>

    <h1 class="product-title">
      <span class="product-name product-name--main">Korvala</span>
      <span class="product-name product-name--type">GIN</span>
    </h1>

    <p class="alcohol">18,5 % ALKOHOL</p>
    <p class="origin">GEBRAUT &amp; ABGEFÜLLT IN MUSTERSTADT</p>

    <aside class="side-panel">
      <p class="brewery-name">MUSTER BRAUEREI • MUSTERSTADT</p>
      <p class="brewery-about">
        Eine Craft-Brauerei ist eine Brauerei, die kleine Mengen an Bier herstellt, für gewöhnlich<br>
        viel weniger als große Brauereiunternehmen; üblicherweise handelt es sich um unabhängige<br>
        Unternehmen. Solche Brauereien zeichnen sich in der Regel durch ihren Fokus auf Qualität,<br>
        Geschmack und Brautechnik aus.
      </p>
    </aside>

    <div class="accent-band"></div>
  </main>
</body>
</html>
```